Design Facebook and LinkedIn design for existing company

We have an existing website. We want a modern interactive Facebook and LinkedIn design. Our website is www.CoverLantern.com

Target Market(s)

People aged 30-50. Family oriented

Industry/Entity Type

Life insurance

Font styles to use
Other font styles liked:
• Rubik

Colors
0054AA
0677BA
7BADD7
CADEEF
E8F1F8
00AB8E
00BBA5
67D7C9
C6EFE9
E9F9F6
59FF00
82FF00
B8FF75
E3FFCB
F4FFEA

Requirements
Must have
• It must be modern
Nice to have
• Same color scheme as website
Should not have
• Colors that deviate from our website

```html
<!DOCTYPE html>
<html lang="en">
<head>
<meta charset="utf-8">
<title>CoverLantern Social Covers</title>
<link rel="stylesheet" href="https://fonts.googleapis.com/css2?family=Inter:wght@400;500;700;800&display=swap">
<style>
  :root {
    --navy: #1f2a3c;
    --blue: #0069b0;
    --blue-deep: #006bb3;
    --green: #8dc63f;
    --mist: #eceff1;
    --white: #ffffff;
    --ink: #111111;
    --bg-top: #ffffff;
    --bg-bottom: #e3e3e3;
  }
  * { margin: 0; padding: 0; box-sizing: border-box; }
  html, body {
    width: 1200px;
    height: 1200px;
    overflow: hidden;
  }
  body {
    position: relative;
    background: linear-gradient(180deg, var(--bg-top) 0%, var(--bg-bottom) 100%);
    font-family: "Inter", Arial, sans-serif;
  }
  .board-label {
    position: absolute;
    left: 0;
    width: 1200px;
    text-align: center;
    font-size: 25px;
    font-weight: 700;
    color: var(--ink);
    letter-spacing: 0.1px;
  }
  .label-facebook { top: 103px; }
  .label-linkedin { top: 652px; }
  .cover {
    position: absolute;
    left: 122px;
    width: 956px;
    box-shadow: 0 14px 18px rgba(0, 0, 0, 0.28);
    background: var(--navy);
  }
  .cover svg { display: block; overflow: visible; }
  .cover-facebook { top: 168px; height: 354px; }
  .cover-linkedin { top: 712px; height: 290px; }
  .headline { font-family: "Inter", Arial, sans-serif; letter-spacing: -2px; }
  .headline-bold { font-weight: 800; }
  .headline-light { font-weight: 400; }
  .tagline { font-family: "Inter", Arial, sans-serif; font-weight: 500; letter-spacing: 2.5px; }
  .cta-label { font-family: "Inter", Arial, sans-serif; font-weight: 500; }
  .brand-name { font-family: "Inter", Arial, sans-serif; font-weight: 400; }
  .web-address { font-family: "Inter", Arial, sans-serif; font-weight: 400; letter-spacing: 1px; }
</style>
</head>
<body>

  <h2 class="board-label label-facebook">Facebook Cover</h2>

  <div class="cover cover-facebook">
    <svg viewBox="0 0 1539 570" width="956" height="354" aria-label="Facebook cover for CoverLantern online life insurance">
      <defs>
        <clipPath id="fb-clip"><rect width="1539" height="570"/></clipPath>
      </defs>
      <g clip-path="url(#fb-clip)">
        <rect class="cover-bg" width="1539" height="570" fill="var(--navy)"/>
        <circle class="accent-disc" cx="201" cy="91" r="235" fill="var(--mist)"/>
        <circle class="accent-top" cx="1042" cy="1" r="118" fill="var(--blue)"/>
        <circle class="accent-dot" cx="1279" cy="224" r="48" fill="var(--green)"/>
        <path class="wave-green" fill="var(--green)"
          d="M634 570 C 790 525, 900 420, 1015 390 C 1100 372, 1240 380, 1300 375 C 1430 362, 1500 262, 1539 165 L1539 570 Z"/>
        <path class="wave-blue" fill="var(--blue-deep)"
          d="M924 570 C 980 510, 1020 462, 1100 452 C 1180 442, 1300 452, 1360 440 C 1460 418, 1510 320, 1539 235 L1539 570 Z"/>
      </g>

      <text class="headline headline-bold" x="108" y="137" font-size="96" fill="var(--blue)">Online</text>
      <text class="headline headline-light" x="438" y="137" font-size="96" fill="var(--green)">Life</text>
      <text class="headline headline-bold" x="120" y="234" font-size="100" fill="var(--green)">Insurance</text>

      <text class="tagline" x="134" y="369" font-size="22" fill="var(--green)">APPLY IN MINUTES</text>
      <g class="tick-icon" fill="none" stroke="var(--green)" stroke-width="2.5" stroke-linecap="round" stroke-linejoin="round">
        <circle cx="399" cy="359" r="17"/>
        <path d="M391 359 l6 6 l10 -11"/>
      </g>

      <g class="cta">
        <rect x="796" y="222" width="256" height="64" rx="32" fill="var(--green)"/>
        <text class="cta-label" x="924" y="262" font-size="25" fill="var(--white)" text-anchor="middle">Compare Quotes</text>
      </g>

      <text class="brand-name" x="1492" y="80" font-size="38" fill="var(--white)" text-anchor="end">CoverLantern</text>

      <text class="web-address" x="1456" y="537" font-size="31" fill="var(--white)" text-anchor="end">www.CoverLantern.com</text>

      <g class="profile-badge">
        <circle cx="261" cy="570" r="147" fill="var(--white)"/>
        <circle cx="261" cy="570" r="127" fill="var(--mist)" stroke="var(--blue)" stroke-width="4"/>
        <text class="brand-name" x="261" y="580" font-size="30" fill="var(--blue)" text-anchor="middle">CoverLantern</text>
      </g>
    </svg>
  </div>

  <h2 class="board-label label-linkedin">LinkedIn Cover</h2>

  <div class="cover cover-linkedin">
    <svg viewBox="0 0 1539 467" width="956" height="290" aria-label="LinkedIn cover for CoverLantern online life insurance">
      <defs>
        <clipPath id="li-clip"><rect width="1539" height="467"/></clipPath>
      </defs>
      <g clip-path="url(#li-clip)">
        <rect class="cover-bg" width="1539" height="467" fill="var(--navy)"/>
        <circle class="accent-disc" cx="171" cy="75" r="200" fill="var(--green)"/>
        <circle class="accent-top" cx="1040" cy="-1" r="110" fill="var(--blue)"/>
        <circle class="accent-dot" cx="1235" cy="205" r="50" fill="var(--green)"/>
        <path class="wave-green" fill="var(--green)"
          d="M739 467 C 880 430, 960 360, 1060 315 C 1130 292, 1250 295, 1310 292 C 1440 285, 1500 200, 1539 110 L1539 467 Z"/>
        <path class="wave-blue" fill="var(--blue-deep)"
          d="M996 467 C 1040 420, 1070 385, 1130 375 C 1200 364, 1310 368, 1370 358 C 1465 340, 1510 260, 1539 190 L1539 467 Z"/>
      </g>

      <text class="headline headline-bold" x="141" y="108" font-size="74" fill="var(--blue)">Online</text>
      <text class="headline headline-light" x="376" y="108" font-size="74" fill="var(--green)">Life</text>
      <text class="headline headline-bold" x="148" y="181" font-size="76" fill="var(--white)">Insurance</text>

      <text class="tagline" x="159" y="234" font-size="21" fill="var(--white)">APPLY IN MINUTES</text>
      <g class="tick-icon" fill="none" stroke="var(--white)" stroke-width="2.5" stroke-linecap="round" stroke-linejoin="round">
        <circle cx="424" cy="225" r="17"/>
        <path d="M416 225 l6 6 l10 -11"/>
      </g>

      <g class="cta">
        <rect x="659" y="195" width="252" height="64" rx="32" fill="var(--green)"/>
        <text class="cta-label" x="785" y="234" font-size="25" fill="var(--white)" text-anchor="middle">Compare Quotes</text>
      </g>

      <text class="brand-name" x="1492" y="77" font-size="38" fill="var(--white)" text-anchor="end">CoverLantern</text>

      <text class="web-address" x="1456" y="438" font-size="31" fill="var(--white)" text-anchor="end">www.CoverLantern.com</text>

      <g class="profile-badge">
        <circle cx="237" cy="454" r="132" fill="var(--white)"/>
        <circle cx="237" cy="454" r="115" fill="var(--mist)"/>
        <circle cx="237" cy="454" r="92" fill="none" stroke="var(--blue)" stroke-width="3"/>
        <text class="brand-name" x="237" y="462" font-size="23" fill="var(--blue)" text-anchor="middle">CoverLantern</text>
      </g>
    </svg>
  </div>

</body>
</html>
```